Pasta Sauce Label for Kestrel Sauce

We need a label for our pasta sauce. We already have a logo and business card designs that i can attach for inspiration and consistency. Looking to use neutral colors, beiges, whites, plus our main color green. you can also see some of our design elements on our website. www.thekestrelsauce-example.com
Also we need space to put nutrition labels and UPC codes as well. I don't have the information for those just yet.
The label will be printed on recycled wood or other material. So the background not being a specific color would be helpful in making it "pop".
Thanks!
Food Production

```html
<!DOCTYPE html>
<html lang="en">
<head>
<meta charset="utf-8">
<title>Kestrel Sauce – Pasta Sauce Labels</title>
<link href="https://fonts.googleapis.com/css2?family=Passion+One:wght@700&family=Parisienne&family=Zilla+Slab:wght@500;600&family=Raleway:wght@500&display=swap" rel="stylesheet">
<style>
  :root {
    --page: #f3f3f3;
    --green: #1fbf63;
    --green-dark: #12904a;
    --ink: #3a3236;
    --ink-black: #1c1a1b;
    --white: #ffffff;
    --silver-1: #e4e4e4;
    --silver-2: #c9c9c9;
    --kraft-1: #d8c7a3;
    --kraft-2: #c4ae86;
    --tomato-1: #e2432a;
    --tomato-2: #a81b12;
    --gold: #e3b23c;
    --panel: rgba(255,255,255,0.55);
  }
  * { box-sizing: border-box; margin: 0; padding: 0; }
  html, body { width: 1200px; height: 907px; overflow: hidden; background: var(--page); }
  .canvas { position: relative; width: 1200px; height: 907px; }

  .label { position: absolute; top: 193px; width: 540px; height: 520px; overflow: hidden; }
  .label--silver { left: 40px; }
  .label--kraft { left: 620px; }

  .label__ground { position: absolute; inset: 0; }
  .label--silver .label__ground { background: linear-gradient(180deg, var(--silver-1), var(--silver-2)); }
  .label--kraft .label__ground { background: linear-gradient(180deg, var(--kraft-1), var(--kraft-2)); }

  .label__band { position: absolute; left: 0; right: 0; height: 18px; background: var(--white); }
  .label__band::before, .label__band::after { content: ""; position: absolute; left: 0; right: 0; }
  .label__band::before { height: 6px; background: var(--green); }
  .label__band::after { height: 2px; background: var(--ink-black); }
  .label__band--top { top: 0; }
  .label__band--top::before { top: 3px; } .label__band--top::after { bottom: 0; }
  .label__band--bottom { bottom: 0; }
  .label__band--bottom::before { bottom: 3px; } .label__band--bottom::after { top: 0; }

  .brand-tab {
    position: absolute; left: 82px; top: 10px; width: 185px; height: 130px;
    background: var(--green); border-radius: 0 0 18px 18px;
    display: flex; align-items: center; justify-content: center;
  }
  .brand-tab__name { font-family: "Raleway", sans-serif; font-weight: 500; font-size: 19px; color: var(--white); letter-spacing: 0.5px; }

  .tomato-photo {
    position: absolute; left: 292px; top: 38px; width: 155px; height: 97px;
    border-radius: 50%; background: radial-gradient(circle at 40% 40%, var(--tomato-1), var(--tomato-2));
  }

  .title { position: absolute; left: 0; right: 0; text-align: center; font-family: "Passion One", sans-serif; font-weight: 700; color: var(--ink); line-height: 1; letter-spacing: 4px; text-shadow: 4px 4px 0 rgba(0,0,0,0.25); }
  .label--kraft .title { color: var(--ink-black); }
  .title--first { top: 150px; font-size: 96px; }
  .title--second { top: 242px; font-size: 100px; }

  .subtitle { position: absolute; left: 160px; top: 340px; font-family: "Parisienne", cursive; font-size: 36px; color: var(--green); }
  .label--kraft .subtitle { color: var(--white); }

  .seal { position: absolute; left: 403px; top: 330px; width: 58px; height: 58px; border-radius: 50%; background: var(--gold); box-shadow: 0 0 0 3px #c99321 inset; }

  .info {
    position: absolute; left: 150px; top: 400px; width: 322px; height: 100px;
    background: var(--panel); border-radius: 4px; padding: 10px 0 0 0;
  }
  .info__line { font-family: "Zilla Slab", serif; color: var(--ink-black); white-space: nowrap; }
  .info__line--claim { font-size: 19px; font-weight: 500; letter-spacing: 0.5px; padding-left: 2px; }
  .info__line--bar { margin: 6px 0 6px 6px; width: 310px; background: var(--ink-black); color: var(--green); font-size: 15px; font-weight: 600; text-align: center; padding: 2px 0; letter-spacing: 0.4px; }
  .info__line--weight { font-size: 21px; font-weight: 500; padding-left: 2px; }

  .origin { position: absolute; left: 45px; top: 390px; width: 100px; height: 100px; border-radius: 50%; background: var(--white); }
  .origin__map { position: absolute; left: 10px; top: 10px; width: 80px; height: 80px; border-radius: 50%; background: var(--green); }
  .origin__place { position: absolute; left: 10px; top: 14px; width: 80px; text-align: center; font-family: "Zilla Slab", serif; font-size: 6px; color: var(--white); }
</style>
</head>
<body>
<div class="canvas">
  <section class="label label--silver">
    <div class="label__ground" role="img" aria-label="Whitewashed wood texture with sketched vegetables along the sides"></div>
    <div class="label__band label__band--top"></div>
    <div class="brand-tab"><span class="brand-tab__name">KESTREL SAUCE</span></div>
    <div class="tomato-photo" role="img" aria-label="Photo of a whole and a halved tomato"></div>
    <div class="title title--first">KESTREL</div>
    <div class="title title--second">SAUCE</div>
    <div class="subtitle">Pasta Sauce</div>
    <div class="seal" role="img" aria-label="Award seal"></div>
    <div class="info">
      <p class="info__line info__line--claim" style="padding-left:8px">100% NATURAL BOTANICALS</p>
      <p class="info__line info__line--bar">ENHANCED TASTE OF YOUR FOOD</p>
      <p class="info__line info__line--weight" style="padding-left:8px">Handcrafted | e 24OZ | 680G</p>
    </div>
    <div class="origin">
      <div class="origin__map" role="img" aria-label="Map of the United States"></div>
      <span class="origin__place">Elm Road, Millbrook, TX</span>
    </div>
    <div class="label__band label__band--bottom"></div>
  </section>

  <section class="label label--kraft">
    <div class="label__ground" role="img" aria-label="Kraft paper texture with sketched vegetables and tomatoes along the sides"></div>
    <div class="label__band label__band--top"></div>
    <div class="brand-tab"><span class="brand-tab__name">KESTREL SAUCE</span></div>
    <div class="tomato-photo" role="img" aria-label="Photo of a whole and a halved tomato"></div>
    <div class="title title--first">KESTREL</div>
    <div class="title title--second">SAUCE</div>
    <div class="subtitle">Pasta Sauce</div>
    <div class="seal" role="img" aria-label="Award seal"></div>
    <div class="info">
      <p class="info__line info__line--claim" style="padding-left:8px">100% NATURAL BOTANICALS</p>
      <p class="info__line info__line--bar">ENHANCED TASTE OF YOUR FOOD</p>
      <p class="info__line info__line--weight" style="padding-left:8px">Handcrafted | e 24OZ | 680G</p>
    </div>
    <div class="origin">
      <div class="origin__map" role="img" aria-label="Map of the United States"></div>
      <span class="origin__place">Elm Road, Millbrook, TX</span>
    </div>
    <div class="label__band label__band--bottom"></div>
  </section>
</div>
</body>
</html>
```